Harborview Behavioral and Community Services

Intellectual Developmental Disabilities, Group Homes, Residential Homes and Substance Abuse Residential facilities

Target Market(s)

Adults 18-59 male and female autism, developmental disabilities and mental health

Industry/Entity Type

Intellectual Development Disabilities, Autism, Applied Behavioral Analysis, Mental Health, Substance Abuse

Coding

Coded - Design and coding required

Number of Pages Required

5+ page

Font styles to use
Serif

Colors
0054AA
0677BA
7BADD7
CADEEF
E8F1F8

Requirements
Should not have
• Not specified

```html
<!DOCTYPE html>
<html lang="en">
<head>
<meta charset="utf-8">
<title>Harborview Community Programs</title>
<link href="https://fonts.googleapis.com/css2?family=Lato:wght@400;700;900&display=swap" rel="stylesheet">
<style>
:root{
  --blue-deep:#0054AA;
  --blue:#0a62b6;
  --blue-mid:#0677BA;
  --blue-soft:#7BADD7;
  --blue-pale:#CADEEF;
  --blue-mist:#E8F1F8;
  --ink:#111111;
  --text:#4a4a4a;
  --white:#ffffff;
  --footer:#000000;
}
*{box-sizing:border-box;margin:0;padding:0}
html,body{width:1200px;height:3986px;overflow:hidden}
body{font-family:'Lato',sans-serif;color:var(--text);background:var(--white);position:relative}
.abs{position:absolute}
.btn{position:absolute;display:flex;align-items:center;justify-content:center;border-radius:22px;font-size:15px;color:var(--white);background:var(--blue);height:38px}
.btn.dark{background:#000}
/* header */
.site-header{position:absolute;left:0;top:0;width:1200px;height:85px;background:var(--white)}
.brand{position:absolute;left:111px;top:22px;display:flex;align-items:center;gap:12px}
.brand-dot{width:36px;height:36px;border-radius:50%;background:var(--blue)}
.brand-name{font-weight:900;font-size:16px;line-height:19px;color:#0b2a5a;text-transform:uppercase}
.nav{position:absolute;left:464px;top:30px;display:flex;gap:0;font-size:15px;color:#333}
.nav a{padding:4px 12px;border-radius:14px;margin-right:8px}
.nav a.active{background:var(--blue);color:var(--white)}
.apply{left:960px;top:24px;width:129px;height:38px}
/* hero */
.hero{position:absolute;left:0;top:85px;width:1200px;height:665px}
.hero h1{position:absolute;left:108px;top:140px;width:560px;font-weight:900;font-size:38px;line-height:59px;letter-spacing:1px;color:var(--white);text-transform:uppercase}
.hero p{position:absolute;left:111px;top:332px;width:440px;font-size:18px;line-height:25px;color:var(--white)}
.hero .btn{left:111px;top:435px;width:197px}
/* features */
.feature{position:absolute;top:668px;width:315px;height:269px;background:var(--white);box-shadow:0 4px 18px rgba(0,0,0,.1);text-align:center}
.feature svg{margin-top:28px}
.feature h3{font-size:21px;font-weight:700;color:var(--ink);margin-top:12px}
.feature p{font-size:15px;line-height:21px;margin:12px auto 0;width:220px}
.feature .btn{left:94px;top:201px;width:128px}
/* about */
.about-frame{position:absolute;left:125px;top:1032px;width:452px;height:447px}
.about-photo{position:absolute;left:114px;top:1025px;width:438px;height:431px;background:linear-gradient(135deg,#c8cfd6,#9aa5ad 45%,#d6b7a6);border:1px solid #ddd}
.about-copy{position:absolute;left:655px;top:1050px;width:435px;font-size:14.5px;line-height:24px}
.about-copy h2,.section-title{font-weight:700;font-size:40px;color:var(--ink)}
.about-copy h2 span,.section-title span,.footer h4 span{color:var(--blue)}
.about-copy p{margin-top:16px}
.about-copy p:first-of-type{margin-top:22px}
.about-copy b{color:var(--blue);font-weight:400}
/* community */
.community{position:absolute;left:0;top:1541px;width:1200px;height:444px}
.community h2{position:absolute;left:0;top:80px;width:1200px;text-align:center;font-size:40px;font-weight:700;color:var(--white)}
.community p{position:absolute;left:220px;top:160px;width:760px;text-align:center;font-size:19.5px;line-height:30px;color:var(--white)}
.community .btn{left:492px;top:312px;width:215px}
/* services */
.section-title{position:absolute;left:0;width:1200px;text-align:center}
.services-intro{position:absolute;left:285px;top:2123px;width:630px;text-align:center;font-size:14.5px;line-height:24px}
.service{position:absolute;top:2223px;width:308px;height:430px;background:var(--white);box-shadow:0 3px 14px rgba(0,0,0,.1);text-align:center}
.service .photo{position:absolute;left:16px;top:11px;width:278px;height:199px}
.service h3{position:absolute;left:10px;top:246px;width:288px;font-size:19.5px;line-height:25px;font-weight:400;color:var(--ink)}
.service p{position:absolute;left:30px;width:248px;font-size:15px;line-height:21px}
.service .btn{left:90px;top:358px;width:128px}
/* testimonials */
.quote{position:absolute;top:2814px;width:318px;height:229px;background:#fff;border:1px solid #e2e2e2;border-radius:4px;padding:26px 24px}
.quote.active{background:var(--blue);border-color:var(--blue);color:var(--white)}
.quote p{margin-top:18px;font-size:14.5px;line-height:22px}
.quote h4{margin-top:18px;font-size:17px;color:var(--ink)}
.quote.active h4{color:var(--white)}
.quote small{display:block;margin-top:8px;font-size:13px}
.dots{position:absolute;left:562px;top:3086px;display:flex;gap:6px}
.dots i{display:block;width:21px;height:7px;background:#bbb}
.dots i:first-child{background:var(--blue)}
/* resources */
.resources{position:absolute;left:0;top:3179px;width:1200px;height:381px}
.resources h2{position:absolute;left:732px;top:56px;font-size:40px;font-weight:700;color:var(--white)}
.resources p{position:absolute;left:727px;top:135px;width:370px;font-size:15px;line-height:24px;color:var(--white)}
.resources .btn{left:723px;top:277px;width:181px}
/* footer */
.footer{position:absolute;left:0;top:3560px;width:1200px;height:426px;background:var(--footer);color:var(--white)}
.footer h4{position:absolute;top:78px;font-size:20px;font-weight:700}
.footer .col{position:absolute;top:136px;font-size:15px;line-height:26px}
.footer ul{list-style:none}
.footer ul li{height:51.5px}
.contact-row{display:flex;gap:18px;height:58px}
.contact-row svg{flex:none;margin-top:4px}
.socials{position:absolute;left:117px;top:282px;display:flex;gap:20px}
.socials span{width:22px;height:22px;border-radius:4px;background:var(--white)}
.socials span:first-child{background:var(--blue)}
.footer .rule{position:absolute;left:111px;top:375px;width:978px;height:1px;background:#333}
.footer .copy{position:absolute;left:0;top:390px;width:1200px;text-align:center;font-size:13px}
</style>
</head>
<body>

<header class="site-header">
  <div class="brand"><span class="brand-dot"></span><span class="brand-name">Harborview Community<br>Programs</span></div>
  <nav class="nav"><a class="active">Home</a><a>About Us</a><a>Services</a><a>Resources</a><a>Contact Us</a></nav>
  <a class="btn apply">Apply Now</a>
</header>

<section class="hero">
  <svg class="abs" width="1200" height="665" style="left:0;top:0" role="img" aria-label="Caregiver in blue scrubs holding an elderly person's hand">
    <defs>
      <linearGradient id="heroBase" x1="0" y1="0" x2="1" y2="1"><stop offset="0" stop-color="#1d6fc0"/><stop offset="1" stop-color="#3a86cf"/></linearGradient>
      <linearGradient id="heroPhoto" x1="0" y1="0" x2="1" y2="1"><stop offset="0" stop-color="#3f7fc4"/><stop offset=".5" stop-color="#7aa6d2"/><stop offset=".75" stop-color="#b08c82"/><stop offset="1" stop-color="#5c7fa6"/></linearGradient>
    </defs>
    <rect width="1200" height="665" fill="url(#heroBase)"/>
    <polygon points="448,0 1200,0 1200,665 810,665" fill="url(#heroPhoto)"/>
  </svg>
  <h1>Empowering Lives, Building Stronger Communities</h1>
  <p>Providing compassionate care and supportive living for individuals with intellectual disabilities and those on the path to recovery.</p>
  <a class="btn dark">Get Support Today</a>
</section>

<div class="feature" style="left:111px">
  <svg width="56" height="66" viewBox="0 0 56 66" fill="none" stroke="#0a62b6" stroke-width="2.5"><path d="M4 28 28 6l24 22M10 24v38h36V24"/><circle cx="22" cy="36" r="4"/><path d="M22 42v10h10l4 8"/><circle cx="30" cy="54" r="7"/></svg>
  <h3>Safe &amp; Supportive Homes</h3>
  <p>Comfortable environments for growth and recovery.</p>
  <a class="btn">Read More</a>
</div>
<div class="feature" style="left:442px">
  <svg width="70" height="66" viewBox="0 0 70 66" fill="none" stroke="#0a62b6" stroke-width="2.5"><path d="M35 22c-6-14-28-12-26 4 1 10 14 18 26 28 12-10 25-18 26-28 2-16-20-18-26-4z"/><path d="M6 40l12 14 8 10M64 40 52 54l-8 10"/></svg>
  <h3>Compassionate Care</h3>
  <p>Personalized support for every individual's needs.</p>
  <a class="btn">Read More</a>
</div>
<div class="feature" style="left:772px">
  <svg width="66" height="66" viewBox="0 0 66 66" fill="none" stroke="#0a62b6" stroke-width="2.5"><circle cx="33" cy="38" r="16"/><circle cx="33" cy="38" r="10"/><path d="m28 38 4 4 7-8"/><path d="m33 2 3 6 6 1-5 4 1 6-5-3-5 3 1-6-5-4 6-1zM10 16l2 4 4 1-3 3 1 4-4-2-4 2 1-4-3-3 4-1zM56 16l2 4 4 1-3 3 1 4-4-2-4 2 1-4-3-3 4-1z"/></svg>
  <h3>Experienced Professionals</h3>
  <p>Dedicated experts providing quality care.</p>
  <a class="btn">Read More</a>
</div>

<svg class="about-frame" width="462" height="460" viewBox="0 0 462 460" style="left:120px;top:1030px"><polygon points="440,0 458,0 400,440 5,452 10,440" fill="var(--blue)"/></svg>
<div class="about-photo" role="img" aria-label="Elderly woman in a wheelchair holding hands with a smiling caregiver"></div>
<div class="about-copy">
  <h2>About <span>Us</span></h2>
  <p>At <b>Harborview Community Programs</b>, we are dedicated to providing compassionate care and supportive living environments for individuals with intellectual and developmental disabilities (IDD) and those on the path to substance abuse recovery.</p>
  <p>Our mission is to empower lives, promote independence, and build stronger communities through high-quality residential care and personalized support services. With a team of experienced professionals, we ensure that every individual receives the care, respect, and encouragement they deserve.</p>
</div>
<a class="btn" style="left:656px;top:1383px;width:128px">Read More</a>

<section class="community">
  <div class="abs" role="img" aria-label="Group of caregivers and residents joining hands, tinted blue" style="left:0;top:0;width:1200px;height:444px;background:linear-gradient(100deg,#1a62ae,#2a77c4 50%,#1b67b5)"></div>
  <h2>Community Programs – Get Involved Today!</h2>
  <p>At Harborview Community Programs, we offer a range of supportive and engaging programs designed to empower individuals, promote independence, and build a strong sense of community. Whether you're looking for residential care, skill development, or recovery support, we are here to help!</p>
  <a class="btn dark">Explore Our Programs</a>
</section>

<h2 class="section-title" style="top:2058px">Our <span>Services</span></h2>
<p class="services-intro">At Harborview Community Programs, we provide compassionate, high-quality support tailored to the unique needs of each individual. Our services are designed to foster independence, dignity, and well-being in a safe and nurturing environment.</p>

<div class="service" style="left:111px">
  <div class="photo" role="img" aria-label="Caregiver and young man sharing a warm moment in a playroom" style="background:linear-gradient(135deg,#e9a24a,#3d6fb0 55%,#9a6b5a)"></div>
  <h3>Intellectual &amp; Developmental Disabilities (IDD) Support</h3>
  <p style="top:306px">Personalized care and programs to enhance independence and</p>
  <a class="btn">Read More</a>
</div>
<div class="service" style="left:447px">
  <div class="photo" role="img" aria-label="Residents talking together in a shared home kitchen" style="background:linear-gradient(135deg,#cfd3cf,#6e8b78 50%,#a96a52)"></div>
  <h3 style="top:258px">Group &amp; Residential Homes</h3>
  <p style="top:292px">Safe, structured, and nurturing living environments for individuals in need of support.</p>
  <a class="btn">Read More</a>
</div>
<div class="service" style="left:781px">
  <div class="photo" role="img" aria-label="Two people embracing during a recovery group session" style="background:linear-gradient(135deg,#d8dde2,#7a8a9a 50%,#4f6a88)"></div>
  <h3>Substance Abuse Residential Facilities</h3>
  <p style="top:306px">Compassionate recovery programs focused on healing and long-term</p>
  <a class="btn">Read More</a>
</div>

<h2 class="section-title" style="top:2725px">What Our <span>Customers Say</span></h2>
<svg width="0" height="0" style="position:absolute"><defs><symbol id="star" viewBox="0 0 14 14"><path d="m7 0 2 5h5l-4 3 1.6 5L7 10l-4.6 3L4 8 0 5h5z"/></symbol></defs></svg>
<div class="quote" style="left:111px">
  <svg width="74" height="14" fill="#f5a623"><use href="#star"/><use href="#star" x="15"/><use href="#star" x="30"/><use href="#star" x="45"/><use href="#star" x="60"/></svg>
  <p>Excepteur sint occaecat cupidatat non proident, sunt in culpa qui officia deserunt mollit anim id est laborum.</p>
  <h4>Whitfield</h4><small>Mar 24 2025</small>
</div>
<div class="quote active" style="left:441px">
  <svg width="74" height="14" fill="#ffffff"><use href="#star"/><use href="#star" x="15"/><use href="#star" x="30"/><use href="#star" x="45"/><use href="#star" x="60"/></svg>
  <p>Excepteur sint occaecat cupidatat non proident, sunt in culpa qui officia deserunt mollit anim id est laborum.</p>
  <h4>Marisol</h4><small>Mar 24 2025</small>
</div>
<div class="quote" style="left:771px">
  <svg width="74" height="14" fill="#f5a623"><use href="#star"/><use href="#star" x="15"/><use href="#star" x="30"/><use href="#star" x="45"/><use href="#star" x="60"/></svg>
  <p>Excepteur sint occaecat cupidatat non proident, sunt in culpa qui officia deserunt mollit anim id est laborum.</p>
  <h4>Georgina</h4><small>Mar 24 2025</small>
</div>
<div class="dots"><i></i><i></i><i></i></div>

<section class="resources">
  <svg class="abs" width="1200" height="381" style="left:0;top:0" role="img" aria-label="Two people sharing a comforting hug">
    <defs><linearGradient id="resPhoto" x1="0" y1="0" x2="1" y2="0"><stop offset="0" stop-color="#3b3a36"/><stop offset=".35" stop-color="#b8a486"/><stop offset=".6" stop-color="#6a6560"/></linearGradient></defs>
    <rect width="1200" height="381" fill="url(#resPhoto)"/>
    <polygon points="726,0 1200,0 1200,381 345,381" fill="#1f70c0"/>
  </svg>
  <h2>Resources &amp; Blog</h2>
  <p>Our resource center provides valuable articles, guides, and expert insights to help individuals, families, and caregivers navigate the journey of intellectual and developmental disabilities, residential care, and substance abuse recovery.</p>
  <a class="btn dark">Explore Resources</a>
</section>

<footer class="footer">
  <h4 style="left:111px">About <span>Us</span></h4>
  <div class="col" style="left:111px;width:230px">Harborview Community Programs – Supporting individuals with IDD, residential care, and recovery for a brighter future.</div>
  <div class="socials"><span aria-label="Social link"></span><span aria-label="Social link"></span><span aria-label="Social link"></span><span aria-label="Social link"></span></div>

  <h4 style="left:439px">Main <span>Links</span></h4>
  <ul class="col" style="left:439px"><li>Home</li><li>About Us</li><li>Services</li><li>Contact Us</li></ul>

  <h4 style="left:629px">Contact <span>Us</span></h4>
  <div class="col" style="left:629px;width:250px">
    <div class="contact-row"><svg width="18" height="20" viewBox="0 0 18 20" fill="none" stroke="#fff" stroke-width="1.5"><path d="M9 19s7-7 7-11A7 7 0 0 0 2 8c0 4 7 11 7 11z"/><circle cx="9" cy="8" r="2.5"/></svg><span>48 Harbor Lane, Suite 210, Bayside 12345.</span></div>
    <div class="contact-row" style="height:64px"><svg width="18" height="18" viewBox="0 0 18 18" fill="none" stroke="#fff" stroke-width="1.5"><path d="M3 1h4l2 4-2.5 1.5a10 10 0 0 0 5 5L13 9l4 2v4a2 2 0 0 1-2 2A15 15 0 0 1 1 3a2 2 0 0 1 2-2z"/></svg><span>+ 1 555 010 2040</span></div>
    <div class="contact-row"><svg width="18" height="14" viewBox="0 0 18 14" fill="none" stroke="#fff" stroke-width="1.5"><rect x="1" y="1" width="16" height="12" rx="1"/><path d="m1 2 8 6 8-6"/></svg><span>info@harborviewcare.org</span></div>
  </div>

  <h4 style="left:957px">Other <span>Links</span></h4>
  <ul class="col" style="left:957px"><li>Admissions</li><li>Resources</li><li>Terms &amp; Conditions</li><li>Privacy Policy</li></ul>

  <div class="rule"></div>
  <div class="copy">Copyright © 2025 Harborview Community Programs All rights reserved.</div>
</footer>

</body>
</html>
```